Poster Design Project

Hi Guys

I am needing an A3 poster design; I basically need a wall chart/ poster that teachers our bakeries how to make the perfect Scone.

I would like our "Flourent" branding to be prominent and these will be hung on bakery production areas for people to utilise when making scones.

Whilst the information needs to be clear I would also like it to be pleasing to the eye and have a "bakery' feel.

Many thanks in advance.

Dave

Target Market(s)

Bakery Production area.

Industry/Entity Type

Bakery

```html
<!DOCTYPE html>
<html lang="en">
<head>
<meta charset="utf-8">
<title>Scone Perfection – Flourent</title>
<link rel="stylesheet" href="https://fonts.googleapis.com/css2?family=Cabin:wght@400&family=Questrial&display=swap">
<style>
:root{
  --paper:#eeefed;
  --outer:#dde2e6;
  --tan:#e9bc72;
  --tan-dark:#c89040;
  --brown:#5b3b17;
  --navy:#1f3f78;
  --stripe:#b3bfd5;
  --photo-a:#8f8a82;
  --photo-b:#cfc3a4;
}
*{margin:0;padding:0;box-sizing:border-box}
html,body{width:849px;height:1200px;overflow:hidden;background:var(--outer)}
body{font-family:"Questrial",sans-serif;color:var(--brown);position:relative}
.frame{position:absolute;inset:0}
.side-ribbon{position:absolute;left:58px;top:0;width:28px;height:715px;
  background:linear-gradient(90deg,#c7d0e0,var(--stripe),#c7d0e0);
  clip-path:polygon(0 0,100% 0,100% 100%,50% 96%,0 100%)}
.title-banner{position:absolute;left:115px;top:12px;width:620px;height:112px;
  background:var(--tan);box-shadow:0 2px 4px rgba(0,0,0,.25);
  clip-path:polygon(0 0,100% 0,96% 50%,100% 100%,0 100%,4% 50%)}
.title-banner::before{content:"";position:absolute;left:28px;right:28px;top:6px;bottom:6px;
  border-top:1px dashed rgba(255,255,255,.8);border-bottom:1px dashed rgba(255,255,255,.8)}
.title-icon{position:absolute;left:64px;top:14px;width:62px;height:54px;border-radius:50%;
  background:rgba(255,255,255,.35)}
.title{position:absolute;left:136px;top:14px;font-size:44px;color:#fff;font-weight:400;
  border-bottom:2px solid #fff;line-height:1.1;padding-bottom:2px}
.subtitle{position:absolute;left:0;right:0;top:70px;text-align:center;font-size:24px;color:#fff}
.step{position:absolute;left:10px;width:812px;background:var(--tan);
  box-shadow:0 3px 5px rgba(0,0,0,.3);
  clip-path:polygon(0 0,100% 0,96.5% 50%,100% 100%,0 100%)}
.step::before{content:"";position:absolute;left:6px;right:6px;top:5px;bottom:5px;
  border-top:1px dashed rgba(255,255,255,.75);border-bottom:1px dashed rgba(255,255,255,.75)}
.step-number{position:absolute;left:30px;width:44px;height:44px;border-radius:50%;
  background:var(--navy);color:#fff;font-size:32px;text-align:center;line-height:44px;
  top:50%;margin-top:-22px}
.step-photo{position:absolute;top:9px;bottom:9px;width:150px;border:2px solid #fff;
  background:linear-gradient(135deg,var(--photo-a),var(--photo-b))}
.step-photo.first{left:87px}.step-photo.second{left:260px}
.step-text{position:absolute;left:426px;width:350px;top:8px;list-style:none;
  font-family:"Cabin",sans-serif;font-size:15px;line-height:19px}
.step-text li{padding-left:9px;text-indent:-9px;margin-bottom:6px}
.step-text li::before{content:"•"}
.step-text.tight li{margin-bottom:1px}
.recipe-banner{position:absolute;left:20px;top:940px;width:810px;height:66px;background:var(--tan-dark);
  clip-path:polygon(0 10%,6% 10%,6% 0,94% 0,94% 10%,100% 10%,96% 50%,100% 90%,94% 90%,94% 100%,6% 100%,6% 90%,0 90%,4% 50%)}
.recipe-table{position:absolute;left:60px;top:940px;width:725px;border-collapse:collapse;font-size:16px}
.recipe-table th{height:66px;color:#fff;font-weight:400;text-align:center;line-height:19px}
.recipe-table th:first-child{text-align:left;padding-left:13px}
.recipe-table th+th{border-left:1px solid rgba(255,255,255,.7)}
.recipe-body{position:absolute;left:60px;top:1006px;width:725px;height:117px;background:var(--tan);border-radius:0 0 8px 8px}
.recipe-table td{height:39px;border-bottom:1px solid rgba(255,255,255,.6);text-align:center}
.recipe-table td+td{border-left:1px solid rgba(255,255,255,.8)}
.recipe-table td:first-child{text-align:left;padding-left:13px}
.recipe-table td:nth-child(2){text-align:left;padding-left:6px}
.recipe-table tr:last-child td{border-bottom:none}
.brand{position:absolute;left:0;right:0;top:1136px;text-align:center}
.brand-name{font-size:54px;color:var(--navy);letter-spacing:1px;line-height:1}
</style>
</head>
<body>
<svg class="frame" width="849" height="1200" viewBox="0 0 849 1200" aria-hidden="true">
  <path d="M52 12 H797 A40 40 0 0 0 837 52 V1148 A40 40 0 0 0 797 1188 H52 A40 40 0 0 0 12 1148 V52 A40 40 0 0 0 52 12 Z" fill="var(--paper)" stroke="#fff" stroke-width="3"/>
</svg>
<div class="side-ribbon" role="img" aria-label="Blue and white striped ribbon"></div>

<header class="title-banner">
  <div class="title-icon" role="img" aria-label="Chef hat icon"></div>
  <h1 class="title">Scone Perfection</h1>
  <p class="subtitle">Best Practice for perfect scone making</p>
</header>

<section class="step" style="top:146px;height:132px">
  <div class="step-number">1</div>
  <div class="step-photo first" role="img" aria-label="Ingredients in mixing bowl with water jug"></div>
  <div class="step-photo second" role="img" aria-label="Mixer bowl with dough hook"></div>
  <ul class="step-text">
    <li>Weigh ingredients into bowl and weigh off cold water into jug</li>
    <li>Add together into bowl</li>
    <li>Mix the ingredients thoroughly on slow speed for 30 seconds using a dough hook</li>
  </ul>
</section>

<section class="step" style="top:291px;height:130px">
  <div class="step-number">2</div>
  <div class="step-photo first" role="img" aria-label="Mixed dough beside bowl of grated cheese"></div>
  <div class="step-photo second" role="img" aria-label="Flavoured scone dough in bowl"></div>
  <ul class="step-text tight" style="top:7px">
    <li>Scrape sides of bowl</li>
    <li>Mix for 15 seconds on second speed Weigh off flavours</li>
    <li>Add to mixed dough, and on slow speed mix thoroughly thru</li>
    <li>Do not over mix</li>
  </ul>
</section>

<section class="step" style="top:436px;height:125px">
  <div class="step-number">3</div>
  <div class="step-photo first" role="img" aria-label="Rounded scone dough on floured bench"></div>
  <div class="step-photo second" role="img" aria-label="Rested dough with round cutter"></div>
  <ul class="step-text">
    <li>Tip onto floured bench and gently round up till a smooth surface</li>
    <li>Do not knead or beat</li>
    <li>Rest for 10 minutes</li>
  </ul>
</section>

<section class="step" style="top:579px;height:130px">
  <div class="step-number">4</div>
  <div class="step-photo first" role="img" aria-label="Dough with rolling pin"></div>
  <div class="step-photo second" role="img" aria-label="Dough rolled out flat"></div>
  <ul class="step-text" style="top:13px">
    <li>Pin / roll out dough gently till you reach your plate size or about 1cm thickness</li>
    <li>Pin / roll out round if using a round cutter to cut down on rework scone dough</li>
  </ul>
</section>

<section class="step" style="top:723px;height:134px">
  <div class="step-number">5</div>
  <div class="step-photo first" role="img" aria-label="Reworked dough offcuts with cutter"></div>
  <div class="step-photo second" role="img" aria-label="Tray of cut scones"></div>
  <ul class="step-text">
    <li>Rework equals tougher scones</li>
    <li>Rework scrape gently, rest before cutting avoid doing this step more than once if possible</li>
    <li>Tray up evenly, rest for 5 minutes</li>
    <li>Bake at &nbsp;210°C -220°C for 15-20minutes</li>
  </ul>
</section>

<div class="recipe-banner"></div>
<div class="recipe-body"></div>
<table class="recipe-table">
  <colgroup><col style="width:153px"><col style="width:57px"><col style="width:85px"><col style="width:120px"><col style="width:92px"><col style="width:71px"><col style="width:147px"></colgroup>
  <thead><tr><th>Scone Recipe</th><th></th><th>Cheese</th><th>Cheese &amp;<br>Onion</th><th>Sultana</th><th>Date</th><th>Spinach &amp; Feta</th></tr></thead>
  <tbody>
    <tr><td>SILKA SCONE MIX</td><td>1.600</td><td></td><td></td><td></td><td></td><td></td></tr>
    <tr><td>Water</td><td>0.900</td><td></td><td></td><td></td><td></td><td></td></tr>
    <tr><td>Total</td><td>2.500</td><td>0.300</td><td>0.200 &amp; 0.100</td><td>0.300</td><td>0.300</td><td>0.200 &amp; 0.100</td></tr>
  </tbody>
</table>

<footer class="brand">
  <span class="brand-name">Flourent</span>
</footer>
</body>
</html>
```